Background Poster for a Exhibition Booth

It's a 9 sqm booth. The design is for the background covering 2 sides, size 120(H) x 300(L) cm each.
Left : about the Greenhouse Agriculture Films/net
Center: Company logo, and overall information
Right: about the Microbial products

Target Market(s)

Farm owner, academy, biotechnology

Industry/Entity Type

Agriculture

Font styles to use
Sans Serif

Colors

Designer to choose colors to be used in the design.

Requirements
Must have
• Company logo at the center

```html
<!DOCTYPE html>
<html lang="en">
<head>
<meta charset="utf-8">
<title>Verdant Root – Booth Backdrop</title>
<link rel="stylesheet" href="https://fonts.googleapis.com/css2?family=Open+Sans:wght@400;600;700&display=swap">
<style>
  :root {
    --page: #2b2b2b;
    --white: #ffffff;
    --paper-top: #ffffff;
    --paper-bottom: #e9e9e9;
    --silver: #b9b9b9;
    --deep-green: #0c5a2a;
    --ring-green: #17703a;
    --brand-green: #05a04f;
    --text-grey: #6d6d6d;
  }
  * { box-sizing: border-box; margin: 0; padding: 0; }
  html, body { width: 1200px; height: 1152px; overflow: hidden; }
  body {
    background: var(--page);
    font-family: "Open Sans", Arial, sans-serif;
    position: relative;
  }
  .panel { position: absolute; left: 54px; width: 1091px; height: 437px; overflow: hidden; }

  /* Center banner */
  .banner-center { top: 79px; background: linear-gradient(180deg, var(--paper-top), var(--paper-bottom)); }
  .banner-center .silver-line {
    position: absolute; left: 0; right: 0; top: 337px; height: 8px;
    background: linear-gradient(90deg, #e0e0e0, var(--silver) 30%, #f4f4f4 50%, var(--silver) 70%, #e0e0e0);
  }
  .banner-center .web-band {
    position: absolute; left: 0; right: 0; bottom: 0; height: 92px;
    background: var(--deep-green);
    display: flex; align-items: center; justify-content: center; gap: 14px;
    color: var(--white); font-weight: 700; font-size: 36px;
  }
  .photo-ring {
    position: absolute; border-radius: 50%;
    border: 4px solid var(--ring-green);
    background: var(--white);
    padding: 9px;
  }
  .photo-ring .photo { width: 100%; height: 100%; border-radius: 50%; }
  .ring-a { left: 38px; top: 58px; width: 230px; height: 230px; z-index: 2; }
  .ring-b { left: 222px; top: 90px; width: 166px; height: 166px; z-index: 1; }
  .ring-c { left: 703px; top: 88px; width: 170px; height: 170px; z-index: 1; }
  .ring-d { left: 829px; top: 56px; width: 232px; height: 232px; z-index: 2; }
  .photo-tunnel { background: linear-gradient(180deg, #cfe0ea 0%, #bcd2c8 40%, #4d8a2f 60%, #2f5e22 100%); }
  .photo-seedbeds { background: linear-gradient(180deg, #c9d1cc 0%, #5e8a52 45%, #355e2d 100%); }
  .photo-racks { background: linear-gradient(160deg, #1f2a22 0%, #3f7a2f 50%, #1e3a1c 100%); }
  .photo-lettuce { background: radial-gradient(circle at 50% 55%, #8ccf45 0%, #4e9a2a 55%, #1e3a16 100%); }

  .brand-mark {
    position: absolute; left: 400px; width: 291px; top: 64px;
    display: flex; flex-direction: column; align-items: center; gap: 28px;
    z-index: 3;
  }
  .brand-mark .dot { width: 124px; height: 124px; border-radius: 50%; background: var(--brand-green); }
  .brand-mark .brand-name {
    font-weight: 700; font-size: 30px; line-height: 36px; letter-spacing: 3px;
    color: var(--text-grey); white-space: nowrap;
  }

  /* Product banner */
  .banner-products { top: 579px; display: flex; }
  .half { position: relative; width: 50%; height: 100%; }
  .half .scene { position: absolute; inset: 0; }
  .scene-greenhouse { background: linear-gradient(180deg, #dce8f2 0%, #b6cbd6 28%, #6f9a52 45%, #3f7d24 70%, #2a5a1a 100%); }
  .scene-harvest { background: linear-gradient(180deg, #6fa6dc 0%, #b9d5ee 22%, #6d8d3f 27%, #c9a468 34%, #b89058 70%, #a88452 100%); }
  .info-box {
    position: absolute; top: 59px; width: 301px; height: 320px;
    background: var(--brand-green); color: var(--white);
    padding: 20px 20px 0 38px;
  }
  .half-films .info-box { left: 246px; }
  .half-microbes .info-box { left: 246px; width: 300px; padding-left: 33px; }
  .info-box h2 { font-weight: 600; font-size: 25px; line-height: 35px; }
  .info-box .lead { font-size: 12.5px; line-height: 18px; margin-top: 14px; }
  .info-box ul { list-style: none; margin-top: 14px; }
  .half-films li { font-weight: 600; font-size: 15px; line-height: 19px; margin-bottom: 12px; display: flex; gap: 10px; align-items: center; }
  .half-microbes .info-box h2 { margin-top: 5px; }
  .half-microbes .lead { margin-top: 6px; }
  .half-microbes ul { margin-top: 16px; }
  .half-microbes li { font-weight: 600; font-size: 14.5px; line-height: 21px; margin-bottom: 13px; display: flex; gap: 8px; align-items: flex-start; }
  .half-microbes li svg { margin-top: 5px; flex: none; }
</style>
</head>
<body>

<section class="panel banner-center">
  <div class="photo-ring ring-a"><div class="photo photo-tunnel" role="img" aria-label="Rows of crops inside a plastic greenhouse tunnel"></div></div>
  <div class="photo-ring ring-b"><div class="photo photo-seedbeds" role="img" aria-label="Young leafy crops growing under greenhouse film"></div></div>

  <div class="brand-mark">
    <span class="dot" aria-hidden="true"></span>
    <span class="brand-name">VERDANT ROOT</span>
  </div>

  <div class="photo-ring ring-c"><div class="photo photo-racks" role="img" aria-label="Stacked hydroponic racks of leafy greens"></div></div>
  <div class="photo-ring ring-d"><div class="photo photo-lettuce" role="img" aria-label="Close-up of fresh green lettuce heads"></div></div>

  <div class="silver-line"></div>
  <div class="web-band">
    <svg width="32" height="32" viewBox="0 0 32 32" fill="none" stroke="#fff" stroke-width="2.4" aria-hidden="true">
      <circle cx="16" cy="16" r="13"/>
      <ellipse cx="16" cy="16" rx="6" ry="13"/>
      <line x1="3" y1="16" x2="29" y2="16"/>
      <path d="M5 9h22M5 23h22"/>
    </svg>
    <span class="web-address">www.verdant-root.com</span>
  </div>
</section>

<section class="panel banner-products">
  <div class="half half-films">
    <div class="scene scene-greenhouse" role="img" aria-label="Strawberry rows under the arched film of a greenhouse tunnel"></div>
    <div class="info-box">
      <h2>Greenhouse<br>Agriculture Films</h2>
      <p class="lead">Professional greenhouse film<br>research and manufacturer since 2012</p>
      <ul>
        <li><svg width="14" height="12" viewBox="0 0 14 12" fill="none" stroke="#fff" stroke-width="2"><path d="M1 6l4 4 8-9"/></svg>Light conversion</li>
        <li><svg width="14" height="12" viewBox="0 0 14 12" fill="none" stroke="#fff" stroke-width="2"><path d="M1 6l4 4 8-9"/></svg>Light diffusion</li>
        <li><svg width="14" height="12" viewBox="0 0 14 12" fill="none" stroke="#fff" stroke-width="2"><path d="M1 6l4 4 8-9"/></svg>Anti-fogging</li>
        <li><svg width="14" height="12" viewBox="0 0 14 12" fill="none" stroke="#fff" stroke-width="2"><path d="M1 6l4 4 8-9"/></svg>Anti-dripping</li>
        <li><svg width="14" height="12" viewBox="0 0 14 12" fill="none" stroke="#fff" stroke-width="2"><path d="M1 6l4 4 8-9"/></svg>Long lifespan</li>
      </ul>
    </div>
  </div>

  <div class="half half-microbes">
    <div class="scene scene-harvest" role="img" aria-label="Tractor and grain trailer beside a combine harvester in a wheat field"></div>
    <div class="info-box">
      <h2>Microbial Products</h2>
      <p class="lead">Change from the root.</p>
      <ul>
        <li><svg width="12" height="11" viewBox="0 0 14 12" fill="none" stroke="#fff" stroke-width="2"><path d="M1 6l4 4 8-9"/></svg><span>GRS-1 Soil Enhancement</span></li>
        <li><svg width="12" height="11" viewBox="0 0 14 12" fill="none" stroke="#fff" stroke-width="2"><path d="M1 6l4 4 8-9"/></svg><span>GRS-2 Hydroculture<br>Growing Medium</span></li>
        <li><svg width="12" height="11" viewBox="0 0 14 12" fill="none" stroke="#fff" stroke-width="2"><path d="M1 6l4 4 8-9"/></svg><span>GRA-1 Aerobic<br>Fermentation Booster</span></li>
        <li><svg width="12" height="11" viewBox="0 0 14 12" fill="none" stroke="#fff" stroke-width="2"><path d="M1 6l4 4 8-9"/></svg><span>GRA-2 Poultry<br>Bedding Enhancement</span></li>
      </ul>
    </div>
  </div>
</section>

</body>
</html>
```